2021 IT Training Presentation Deck Refresh

Copper Lantern is an IT education services firm. We teach IT industry standards and technologies. We are in need of an updated training presentation deck that factors in a fresh take for:

1) Agenda/Table of Contents
2) Chapter Topic Summary
2) Chapter Introduction and Learning Objectives
3) Chapter Recaps
4) Important Point/Pro Tip emphasis
5) Warning Message
6) Mini Quiz layout
7) Lab Exercise Introduction
7) Deck Close Out

Incorporating the official Copper Lantern colour palette for materials that will likely be used in self-paced/online recorded versions of courses.

Target Market(s)

IT

Industry/Entity Type

Computer Training

Requirements
Nice to have
• placeholder sections for images of IT workers in an office or by a computer

```html
<!DOCTYPE html>
<html lang="en">
<head>
<meta charset="utf-8">
<title>Copper Lantern – Training Presentation Deck</title>
<link rel="stylesheet" href="https://fonts.googleapis.com/css2?family=Montserrat:wght@300;400;500;600;700;800&family=Open+Sans:wght@400;600;700&display=swap">
<style>
:root{
  --navy:#27306b;
  --ink:#1e2538;
  --blue:#3d5aa8;
  --mid:#4f74c4;
  --sky:#6b9be0;
  --pale:#9cc8f2;
  --canvas:#e8e9eb;
  --text:#40465a;
  --white:#ffffff;
}
*{margin:0;padding:0;box-sizing:border-box}
html,body{width:1200px;height:3560px;overflow:hidden;background:var(--canvas)}
body{position:relative;font-family:"Open Sans",sans-serif;color:var(--text)}
h1,h2,h3,h4,.head{font-family:"Montserrat",sans-serif}

/* showcase placement */
.hero{position:absolute;left:256px;top:217px;width:551px;height:310px;transform:scale(1.334);transform-origin:0 0;box-shadow:0 8px 30px rgba(20,30,70,.25)}
.deck-grid{position:absolute;left:36px;top:933px;display:grid;grid-template-columns:551px 551px;grid-auto-rows:310px;column-gap:16px;row-gap:15px}

/* slide base */
.slide{position:relative;width:551px;height:310px;overflow:hidden;background:var(--white)}
.abs{position:absolute}
.brand{font-family:"Montserrat",sans-serif;font-weight:500;color:var(--blue);white-space:nowrap}
.brand-mini{position:absolute;top:14px;right:14px;font-size:6px}
.foot{position:absolute;left:0;right:0;bottom:0;height:16px;border-bottom:3px solid var(--navy);font-family:"Montserrat",sans-serif;font-size:4px;letter-spacing:1px;color:var(--ink)}
.foot .copy{position:absolute;left:8px;top:5px}
.foot .page{position:absolute;right:14px;top:5px}
.body{font-size:5.4px;line-height:1.55;color:var(--text)}
.title-dark{font-family:"Montserrat",sans-serif;font-weight:600;color:var(--ink);line-height:1.1}
.photo{position:absolute}

/* title slide */
.ts-photo{position:absolute;left:0;top:0;width:100%;height:240px;background:linear-gradient(180deg,#7089c9 0%,#4d67ae 55%,#33479a 100%)}
.url-pill{position:absolute;left:170px;top:48px;width:200px;height:19px;border-radius:10px;background:var(--navy);color:#dfe6f6;font-family:"Montserrat",sans-serif;font-size:7.5px;letter-spacing:2px;text-align:center;line-height:19px}
.ts-h1{position:absolute;left:0;right:0;top:82px;text-align:center;color:#fff;font-weight:800;font-size:37px;letter-spacing:.5px}
.ts-title{position:absolute;left:0;right:0;top:124px;text-align:center;color:#fff;font-family:"Montserrat",sans-serif;font-weight:300;font-size:28px}
.ts-sub{position:absolute;left:0;right:0;top:160px;text-align:center;color:var(--pale);font-family:"Montserrat",sans-serif;font-weight:300;font-size:15px;letter-spacing:2px}
.date-pill{position:absolute;left:378px;top:229px;width:140px;height:23px;border-radius:12px;background:linear-gradient(90deg,#3d5aa8,#5d84d2);border:1.5px solid #fff;color:#fff;font-family:"Montserrat",sans-serif;font-weight:600;font-size:8px;text-align:center;line-height:20px}
.ts-brand{position:absolute;left:34px;top:275px;font-size:10px}

/* cover two */
.cover2 .topline{position:absolute;left:0;right:0;top:0;height:4px;background:var(--pale)}
.cover2 .brand-c{position:absolute;left:0;right:0;top:100px;text-align:center;font-size:12px}
.cover2 .brand-dot{position:absolute;left:262px;top:62px;width:28px;height:28px;border-radius:50%;background:var(--mid)}
.cover2 h2{position:absolute;left:0;right:0;top:122px;text-align:center;font-weight:800;font-size:36px;color:var(--blue)}
.cover2 .t2{position:absolute;left:0;right:0;top:163px;text-align:center;font-family:"Montserrat",sans-serif;font-weight:700;font-size:22px;color:var(--blue)}
.cover2 .s2{position:absolute;left:0;right:0;top:190px;text-align:center;font-family:"Montserrat",sans-serif;font-size:13px;letter-spacing:1.5px;color:var(--blue)}
.pill-sm{position:absolute;height:15px;border-radius:8px;background:var(--blue);color:#fff;font-family:"Montserrat",sans-serif;font-weight:600;font-size:6px;text-align:center;line-height:15px}

/* agenda */
.agenda .panel{position:absolute;left:0;top:0;width:268px;height:100%;background:linear-gradient(180deg,#4f74c4,#2f3f8c)}
.agenda .card{position:absolute;left:68px;top:46px;width:200px;height:227px;background:#fff;box-shadow:0 4px 14px rgba(0,0,0,.12);padding:14px 0 0 28px}
.agenda ol{font-size:7px;line-height:21.8px;color:var(--ink);padding-left:0;list-style:none;counter-reset:ag}
.agenda li{counter-increment:ag}
.agenda li::before{content:counter(ag)".";color:var(--mid);display:inline-block;width:16px}
.agenda .heading{position:absolute;left:317px;top:98px;font-size:21px}
.agenda .sub{position:absolute;left:317px;top:168px;font-size:8px;color:var(--mid);font-family:"Montserrat",sans-serif}

/* chapter divider */
.divider{background:linear-gradient(180deg,#6a91d6 0%,#4a68b4 55%,#303f8e 100%)}
.divider .brand{position:absolute;left:36px;top:90px;font-size:8px;color:#fff}
.divider h3{position:absolute;left:36px;top:112px;color:#fff;font-size:24px;font-weight:700}
.divider .t{position:absolute;left:36px;top:145px;color:#fff;font-family:"Montserrat",sans-serif;font-weight:300;font-size:19px}
.divider .body{position:absolute;left:36px;top:180px;width:330px;color:#e3ebf8}

/* text three columns */
.txt3 .heading{position:absolute;left:36px;top:44px;font-size:19px}
.txt3 .tag{position:absolute;left:36px;top:121px;font-family:"Montserrat",sans-serif;font-weight:700;font-size:7px;color:var(--navy)}
.txt3 .tag i{display:inline-block;width:16px;height:5px;border-radius:3px;background:var(--blue);margin-right:6px;vertical-align:middle}
.txt3 .rule{position:absolute;left:150px;right:36px;top:125px;height:1px;background:#c8d3ea}
.txt3 .cols{position:absolute;left:36px;right:30px;top:152px;display:grid;grid-template-columns:repeat(3,1fr);gap:17px;text-align:justify}
.txt3 .cols p+p{margin-top:6px}

/* about */
.about .heading{position:absolute;left:46px;top:96px;font-size:18px}
.about .lead{position:absolute;left:46px;top:130px;font-size:6px;color:var(--mid)}
.about .lead b{color:var(--navy)}
.about .body{position:absolute;left:46px;top:160px;width:190px;text-align:justify}
.about .photo{left:260px;top:0;width:291px;height:270px;background:linear-gradient(160deg,#dfe6ee,#b7c4d3 55%,#8f9fb4)}
.about .cap{position:absolute;left:260px;top:218px;width:291px;height:52px;background:linear-gradient(90deg,rgba(61,90,168,.95),rgba(79,116,196,.9));color:#fff;font-size:7px;font-weight:600;padding:12px 18px;line-height:1.35}

/* quote */
.quote .photo{inset:0;background:linear-gradient(180deg,#6d85bf,#465fa6 60%,#2f3f8a)}
.quote .k1{position:absolute;left:0;right:0;top:76px;text-align:center;color:#fff;font-family:"Montserrat",sans-serif;font-weight:300;font-size:18px}
.quote .k2{position:absolute;left:0;right:0;top:100px;text-align:center;color:#fff;font-weight:600;font-size:19px}
.quote .qi{position:absolute;left:264px;top:168px}
.quote .q{position:absolute;left:0;right:0;top:205px;text-align:center;color:#fff;font-family:"Montserrat",sans-serif;font-size:11px;line-height:1.45}
.quote .a{position:absolute;left:0;right:0;top:245px;text-align:center;color:#dbe4f4;font-size:8px;font-style:italic}

/* objectives */
.objectives .photo{left:0;top:0;width:100%;height:100%;background:linear-gradient(135deg,#5574b9,#37499a)}
.objectives .cut{position:absolute;inset:0}
.objectives .heading{position:absolute;left:38px;top:74px;color:#fff;font-size:14px;font-weight:600;line-height:1.2}
.objectives .body{position:absolute;left:38px;top:133px;width:200px;color:#e3ebf8;font-size:4.9px;text-align:justify}
.obj-card{position:absolute;width:124px;height:94px;background:#fff;box-shadow:0 2px 10px rgba(0,0,0,.12);text-align:center;padding-top:12px}
.obj-card h4{font-size:5.8px;color:var(--navy);margin-top:5px}
.obj-card p{font-size:4.8px;line-height:1.5;color:var(--text);margin-top:2px;padding:0 10px}

/* circle photo slides */
.arc .photo{left:0;top:0;width:260px;height:310px;border-radius:0 155px 155px 0/0 155px 155px 0;background:linear-gradient(150deg,#8c7b6b,#5c6477 50%,#2f3a55)}
.arc .heading{position:absolute;left:292px;top:70px;font-size:20px}
.arc .body{position:absolute;left:297px;top:148px;width:215px}
.arc2 .photo{background:linear-gradient(150deg,#e4ded6,#b8aca0 55%,#7d7a7c)}
.arc2 .heading{left:277px;top:63px;font-size:18px}
.stats{position:absolute;left:277px;top:118px;width:237px;height:38px;border:1px solid #d6def0;display:flex;align-items:center;justify-content:space-around}
.stat{text-align:center;font-family:"Montserrat",sans-serif}
.stat b{display:block;font-size:16px;color:var(--navy);line-height:1}
.stat span{font-size:5px}
.stat.hl{background:var(--blue);color:#fff;padding:5px 14px}
.stat.hl b{color:var(--pale)}
.checks{position:absolute;left:277px;top:180px;width:240px;list-style:none}
.checks li{display:flex;gap:7px;font-size:5.2px;line-height:1.45;margin-bottom:14px}
.checks svg{flex:none}

/* important point */
.point .box{position:absolute;left:103px;top:91px;width:346px;height:126px;border-radius:6px;background:linear-gradient(90deg,#2f3f8c,#4f74c4);box-shadow:6px 12px 18px rgba(30,40,90,.25);text-align:center;color:#e4ebf8;padding:18px 26px 0}
.point h3{font-size:18px;color:#fff;font-weight:700;margin-bottom:7px}
.point p{font-size:6.6px;line-height:1.4}
.point p+p{margin-top:5px}

/* projects grid */
.projects .heading{position:absolute;left:36px;top:48px;font-size:18px}
.proj{position:absolute;display:flex;gap:10px;width:210px}
.proj h4{font-size:6px;color:var(--ink);font-weight:600}
.proj p{font-size:5px;line-height:1.45}

/* three cards */
.cards3 .heading{position:absolute;left:36px;top:56px;font-size:19px}
.c3{position:absolute;top:135px;width:126px;height:112px;color:#fff;text-align:center;padding-top:40px}
.c3 .ic{position:absolute;left:47px;top:-16px;width:32px;height:32px;border-radius:50%;background:#fff;display:flex;align-items:center;justify-content:center}
.c3 h4{font-size:6px;font-weight:600}
.c3 p{font-size:5.2px;line-height:1.45;margin-top:3px;padding:0 12px}

/* media slide */
.media .band{position:absolute;left:0;top:92px;width:100%;height:218px;background:linear-gradient(180deg,#6a91d6,#3c5aa8)}
.media .heading{position:absolute;left:36px;top:50px;font-size:18px}
.media .body{position:absolute;left:38px;top:148px;width:190px;color:#eaf0fb;font-size:5.3px}
.media .body p+p{margin-top:6px}
.laptop{position:absolute;left:242px;top:90px;width:300px;height:186px}

/* quiz */
.quiz .heading{position:absolute;left:30px;top:40px;font-size:19px}
.q-bar{position:absolute;left:100px;top:112px;width:356px;height:30px;border-radius:15px;background:linear-gradient(90deg,#2f3f8c,#4f74c4);color:#fff;font-family:"Montserrat",sans-serif;font-weight:600;font-size:11px;text-align:center;line-height:30px}
.ans{position:absolute;width:192px;height:21px;border-radius:11px;background:var(--sky);color:#fff;font-family:"Montserrat",sans-serif;font-weight:600;font-size:10px;text-align:center;line-height:21px}

/* close */
.close .photo{inset:0;background:linear-gradient(180deg,#5a7ac0,#4a66ad 55%,#2c3c86)}
.close .brand{position:absolute;left:0;right:0;top:118px;text-align:center;color:#fff;font-size:20px;font-weight:400}
.close .dot{position:absolute;left:261px;top:76px;width:30px;height:30px;border-radius:50%;background:#fff}
.close .thanks{position:absolute;left:0;right:0;top:215px;text-align:center;color:#fff;font-weight:700;font-size:20px}
.close .thanks span{color:var(--navy)}
.contact{position:absolute;left:66px;right:40px;top:268px;display:flex;justify-content:space-between;color:#e2e9f7;font-size:5px}
.contact span{display:flex;align-items:center;gap:4px}
</style>
</head>
<body>

<section class="hero">
  <div class="slide title-slide">
    <div class="ts-photo" role="img" aria-label="Blue-toned photo of IT trainees working together at laptops"></div>
    <div class="url-pill">WWW.COPPER-LANTERN.COM</div>
    <h1 class="ts-h1">PRESENTATION</h1>
    <p class="ts-title">TITLE GOES HERE</p>
    <p class="ts-sub">Sub Title Goes Here</p>
    <div class="date-pill">Feb 2021</div>
    <div class="brand ts-brand">Copper Lantern</div>
  </div>
</section>

<main class="deck-grid">

  <div class="slide title-slide">
    <div class="ts-photo" role="img" aria-label="Blue-toned photo of IT trainees working together at laptops"></div>
    <div class="url-pill">WWW.COPPER-LANTERN.COM</div>
    <h1 class="ts-h1">PRESENTATION</h1>
    <p class="ts-title">TITLE GOES HERE</p>
    <p class="ts-sub">Sub Title Goes Here</p>
    <div class="date-pill">Feb 2021</div>
    <div class="brand ts-brand">Copper Lantern</div>
  </div>

  <div class="slide cover2">
    <div class="topline"></div>
    <div class="brand-dot"></div>
    <div class="brand brand-c">Copper Lantern</div>
    <h2>PRESENTATION</h2>
    <p class="t2">TITLE GOES HERE</p>
    <p class="s2">Sub Title Goes Here</p>
    <div class="pill-sm" style="left:228px;top:263px;width:94px">Presenter Name</div>
  </div>

  <div class="slide agenda">
    <div class="panel"></div>
    <div class="card">
      <ol>
        <li>Lorem ipsum dolor sit amet</li><li>Lorem ipsum dolor sit amet</li><li>Lorem ipsum dolor sit amet</li>
        <li>Lorem ipsum dolor sit amet</li><li>Lorem ipsum dolor sit amet</li><li>Lorem ipsum dolor sit amet</li>
        <li>Lorem ipsum dolor sit amet</li><li>Lorem ipsum dolor sit amet</li><li>Lorem ipsum dolor sit amet</li>
      </ol>
    </div>
    <div class="brand brand-mini">Copper Lantern</div>
    <h3 class="title-dark heading">Here Goes<br>Title Of Your<br>Agenda</h3>
    <p class="sub">Here Goes A Short Subtitle</p>
    <div class="foot"><span class="page">PAGE | 4</span></div>
  </div>

  <div class="slide divider">
    <div class="brand">Copper Lantern</div>
    <h3>Chapter Devider</h3>
    <p class="t">Title here</p>
    <p class="body">Lorem ipsum dolor sit amet, consectetur adipiscing elit, sed do eiusmod tempor incididunt ut labore et dolore magna aliqua. Ut enim ad minim veniam, quis nostrud exercitation ullamco laboris nisi ut aliquip ex ea commodo consequat duis aute irure dolor.</p>
  </div>

  <div class="slide txt3">
    <div class="brand brand-mini">Copper Lantern</div>
    <h3 class="title-dark heading">Here Add Your Title<br>Short Text Here</h3>
    <p class="tag"><i></i>Your Short Text Here</p>
    <div class="rule"></div>
    <div class="cols body">
      <div><p>Lorem ipsum dolor sit amet, consectetur adipiscing elit, sed do eiusmod tempor incididunt ut labore et dolore magna aliqua.</p><p>Sed do eiusmod tempor incididunt ut labore et dolore.</p><p>Ut enim ad minim veniam, quis nostrud exercitation.</p></div>
      <div><p>Lorem ipsum dolor sit amet, consectetur adipiscing elit, sed do eiusmod tempor incididunt ut labore.</p><p>Consectetur adipiscing elit, sed do eiusmod tempor incididunt ut labore et dolore magna aliqua ut enim ad minim veniam.</p></div>
      <div><p>Lorem ipsum dolor sit amet, consectetur adipiscing elit, sed do eiusmod tempor incididunt ut labore et dolore magna aliqua.</p><p>Consectetur adipiscing elit, sed do eiusmod tempor.</p><p>Ut enim ad minim veniam, quis nostrud exercitation.</p></div>
    </div>
    <div class="foot"><span class="copy">COPYRIGHT © | ALL RIGHTS RESERVED</span><span class="page">PAGE | 6</span></div>
  </div>

  <div class="slide about">
    <h3 class="title-dark heading">About Us</h3>
    <p class="lead">No problem is too big or too small!<br><b>We're here to help.</b></p>
    <p class="body">Lorem ipsum dolor sit amet, consectetur adipiscing elit, sed do eiusmod tempor incididunt ut labore et dolore magna aliqua. Lorem ipsum dolor sit amet, consectetur adipiscing elit, sed do eiusmod tempor incididunt ut labore et dolore magna aliqua. Ut enim ad minim veniam, quis nostrud exercitation ullamco laboris nisi ut aliquip.</p>
    <div class="photo" role="img" aria-label="Photo of two IT workers at desks with computers in a bright office"></div>
    <p class="cap">What you are seeking we have a solution, and if we do not, we know someone who will, this is our promise to you!</p>
    <div class="foot"><span class="copy">COPYRIGHT © | ALL RIGHTS RESERVED</span><span class="page">PAGE | 5</span></div>
  </div>

  <div class="slide quote">
    <div class="photo" role="img" aria-label="Blue-toned photo of a modern training room with hanging lights"></div>
    <p class="k1">Facilitating Process Adoption</p>
    <p class="k2">Learn To Lead</p>
    <svg class="qi" width="22" height="22" viewBox="0 0 22 22"><circle cx="11" cy="11" r="11" fill="#6b9be0"/><path d="M6 13c0-3 1-5 4-6v2c-1 .4-1.6 1.2-1.7 2H10v4H6zm6 0c0-3 1-5 4-6v2c-1 .4-1.6 1.2-1.7 2H16v4h-4z" fill="#fff"/></svg>
    <p class="q">“Our lives are full of days that don’t stand out.<br>Here’s to making today one that does.”</p>
    <p class="a">-Unknown</p>
  </div>

  <div class="slide objectives">
    <div class="photo" role="img" aria-label="Blue-toned photo of hands typing on a laptop keyboard"></div>
    <svg class="cut" viewBox="0 0 551 310" preserveAspectRatio="none"><polygon points="390,0 551,0 551,310 250,310" fill="#fff"/></svg>
    <div class="brand brand-mini">Copper Lantern</div>
    <h3 class="heading">Chapter<br>Introduction and<br>Learning Objectives</h3>
    <p class="body">Copper Lantern was founded with the focus on education and training to promote client success and process adoption. We know firsthand the issues that you face. Our combined experience has helped implement hundreds of IT Service Management initiatives and DeskFlow deployments. We recognized the ongoing challenge that clients have in promoting the adoption of the technologies and processes being implemented.<br><b>Our goal is to truly empower you.</b></p>
    <div class="obj-card" style="left:250px;top:58px"><svg width="16" height="16" viewBox="0 0 16 16"><circle cx="8" cy="8" r="7" fill="none" stroke="#3d5aa8"/><circle cx="8" cy="8" r="3.5" fill="none" stroke="#3d5aa8"/><circle cx="8" cy="8" r="1" fill="#3d5aa8"/></svg><h4>Your Title Goes Here</h4><p>Lorem ipsum dolor sit amet, consectetur adipiscing elit, sed do eiusmod tempor.</p></div>
    <div class="obj-card" style="left:390px;top:58px"><svg width="16" height="16" viewBox="0 0 16 16"><rect x="3" y="2" width="10" height="12" rx="1" fill="none" stroke="#3d5aa8"/><path d="M5 6h6M5 9h6M5 12h4" stroke="#3d5aa8"/></svg><h4>Your Title Goes Here</h4><p>Lorem ipsum dolor sit amet, consectetur adipiscing elit, sed do eiusmod tempor.</p></div>
    <div class="obj-card" style="left:250px;top:163px"><svg width="16" height="16" viewBox="0 0 16 16"><path d="M4 12l3-3M8 3c3 0 5 2 5 5l-4 4-5-5z" fill="none" stroke="#3d5aa8"/></svg><h4>Your Title Goes Here</h4><p>Lorem ipsum dolor sit amet, consectetur adipiscing elit, sed do eiusmod tempor.</p></div>
    <div class="obj-card" style="left:390px;top:163px"><svg width="16" height="16" viewBox="0 0 16 16"><circle cx="8" cy="8" r="7" fill="none" stroke="#3d5aa8"/><circle cx="8" cy="8" r="3.5" fill="none" stroke="#3d5aa8"/><circle cx="8" cy="8" r="1" fill="#3d5aa8"/></svg><h4>Your Title Goes Here</h4><p>Lorem ipsum dolor sit amet, consectetur adipiscing elit, sed do eiusmod tempor.</p></div>
    <div class="foot"><span class="page">PAGE | 8</span></div>
  </div>

  <div class="slide arc">
    <div class="photo" role="img" aria-label="Photo of IT workers coding at computers in an office"></div>
    <div class="brand brand-mini">Copper Lantern</div>
    <h3 class="title-dark heading">Here Goes<br>Title Of This Slide</h3>
    <p class="body">Copper Lantern was founded with the focus on education and training to promote client success and process adoption. We know firsthand the issues that you face. Our combined experience has helped implement hundreds of IT Service Management initiatives and DeskFlow deployments. We recognized the ongoing challenge that clients have in promoting the adoption of the technologies and processes being implemented.<br>Our goal is to truly empower you.</p>
    <div class="foot"><span class="page">PAGE | 9</span></div>
  </div>

  <div class="slide arc arc2">
    <div class="photo" role="img" aria-label="Photo of a person working on a laptop at a desk"></div>
    <div class="brand brand-mini">Copper Lantern</div>
    <h3 class="title-dark heading">Here Add Your Title<br>Short Text Here</h3>
    <div class="stats">
      <div class="stat"><b>950</b><span>Your Text</span></div>
      <div class="stat hl"><b>13%</b><span>Your Text</span></div>
      <div class="stat"><b>0.5M</b><span>Your Text</span></div>
    </div>
    <ul class="checks">
      <li><svg width="8" height="8" viewBox="0 0 8 8"><circle cx="4" cy="4" r="4" fill="#3d5aa8"/><path d="M2.2 4.1l1.2 1.2 2.4-2.6" stroke="#fff" fill="none" stroke-width=".9"/></svg>Lorem ipsum dolor sit amet, nec an dictas equidem appellantur, ut has commune accommodare.</li>
      <li><svg width="8" height="8" viewBox="0 0 8 8"><circle cx="4" cy="4" r="4" fill="#3d5aa8"/><path d="M2.2 4.1l1.2 1.2 2.4-2.6" stroke="#fff" fill="none" stroke-width=".9"/></svg>Lorem ipsum dolor sit amet, nec an dictas equidem appellantur, ut has commune accommodare.</li>
      <li><svg width="8" height="8" viewBox="0 0 8 8"><circle cx="4" cy="4" r="4" fill="#3d5aa8"/><path d="M2.2 4.1l1.2 1.2 2.4-2.6" stroke="#fff" fill="none" stroke-width=".9"/></svg>Lorem ipsum dolor sit amet, nec an dictas equidem appellantur, ut has commune accommodare.</li>
    </ul>
    <div class="foot"><span class="page">PAGE | 11</span></div>
  </div>

  <div class="slide point">
    <div class="brand brand-mini">Copper Lantern</div>
    <div class="box">
      <h3>A Place for Important Point</h3>
      <p>Lorem ipsum dolor sit amet, consectetur adipiscing elit, sed do eiusmod tempor incididunt ut labore et dolore magna aliqua. Lorem ipsum dolor sit amet, consectetur adipiscing elit.</p>
      <p>Sed do eiusmod tempor incididunt ut labore et dolore magna aliqua.</p>
    </div>
    <div class="foot"><span class="copy">COPYRIGHT © | ALL RIGHTS RESERVED</span><span class="page">PAGE | 10</span></div>
  </div>

  <div class="slide projects">
    <div class="brand brand-mini">Copper Lantern</div>
    <h3 class="title-dark heading">Here Add Your Title<br>Short Text Here</h3>
    <div class="proj" style="left:48px;top:112px"><svg width="20" height="20" viewBox="0 0 20 20"><circle cx="10" cy="10" r="10" fill="#3d5aa8"/><circle cx="10" cy="10" r="5" fill="none" stroke="#fff"/></svg><div><h4>Project name</h4><p>Lorem ipsum dolor sit amet, nec an dictas equidem appellantur, ut has commune accommodare. Mea illum.</p></div></div>
    <div class="proj" style="left:288px;top:112px"><svg width="20" height="20" viewBox="0 0 20 20"><circle cx="10" cy="10" r="10" fill="#3d5aa8"/><circle cx="10" cy="10" r="5" fill="none" stroke="#fff"/></svg><div><h4>Project name</h4><p>Lorem ipsum dolor sit amet, nec an dictas equidem appellantur, ut has commune accommodare. Mea illum.</p></div></div>
    <div class="proj" style="left:48px;top:170px"><svg width="20" height="20" viewBox="0 0 20 20"><circle cx="10" cy="10" r="10" fill="#3d5aa8"/><rect x="5.5" y="6" width="9" height="8" fill="none" stroke="#fff"/></svg><div><h4>Project name</h4><p>Lorem ipsum dolor sit amet, nec an dictas equidem appellantur, ut has commune accommodare. Mea illum.</p></div></div>
    <div class="proj" style="left:288px;top:170px"><svg width="20" height="20" viewBox="0 0 20 20"><circle cx="10" cy="10" r="10" fill="#3d5aa8"/><rect x="5.5" y="6" width="9" height="8" fill="none" stroke="#fff"/></svg><div><h4>Project name</h4><p>Lorem ipsum dolor sit amet, nec an dictas equidem appellantur, ut has commune accommodare. Mea illum.</p></div></div>
    <div class="proj" style="left:48px;top:228px"><svg width="20" height="20" viewBox="0 0 20 20"><circle cx="10" cy="10" r="10" fill="#3d5aa8"/><circle cx="10" cy="9" r="3" fill="none" stroke="#fff"/><path d="M6 15h8" stroke="#fff"/></svg><div><h4>Project name</h4><p>Lorem ipsum dolor sit amet, nec an dictas equidem appellantur, ut has commune accommodare. Mea illum.</p></div></div>
    <div class="proj" style="left:288px;top:228px"><svg width="20" height="20" viewBox="0 0 20 20"><circle cx="10" cy="10" r="10" fill="#3d5aa8"/><circle cx="10" cy="9" r="3" fill="none" stroke="#fff"/><path d="M6 15h8" stroke="#fff"/></svg><div><h4>Project name</h4><p>Lorem ipsum dolor sit amet, nec an dictas equidem appellantur, ut has commune accommodare. Mea illum.</p></div></div>
    <div class="foot"><span class="copy">COPYRIGHT © | ALL RIGHTS RESERVED</span><span class="page">PAGE | 13</span></div>
  </div>

  <div class="slide cards3">
    <div class="brand brand-mini">Copper Lantern</div>
    <h3 class="title-dark heading">Here Add Your Title<br>Short Text Here</h3>
    <div class="c3" style="left:62px;background:var(--pale)"><div class="ic"><svg width="16" height="16" viewBox="0 0 16 16"><circle cx="8" cy="6" r="4" fill="none" stroke="#9cc8f2" stroke-width="1.4"/><path d="M6 11h4M6.5 13h3" stroke="#9cc8f2" stroke-width="1.4"/></svg></div><h4>Project name here</h4><p>Lorem ipsum dolor sit amet, nec an dictas equidem appellantur, ut has commune accommodare. Mea illum, ludus solet idpro.</p></div>
    <div class="c3" style="left:203px;background:var(--mid)"><div class="ic"><svg width="16" height="16" viewBox="0 0 16 16"><rect x="3" y="2" width="10" height="12" rx="1" fill="none" stroke="#4f74c4" stroke-width="1.4"/><path d="M5 6h6M5 9h6" stroke="#4f74c4" stroke-width="1.4"/></svg></div><h4>Project name here</h4><p>Lorem ipsum dolor sit amet, nec an dictas equidem appellantur, ut has commune accommodare. Mea illum, ludus solet idpro.</p></div>
    <div class="c3" style="left:344px;background:var(--navy)"><div class="ic"><svg width="16" height="16" viewBox="0 0 16 16"><circle cx="8" cy="5.5" r="3" fill="none" stroke="#27306b" stroke-width="1.4"/><path d="M3 14c0-3 2-5 5-5s5 2 5 5" fill="none" stroke="#27306b" stroke-width="1.4"/></svg></div><h4>Project name here</h4><p>Lorem ipsum dolor sit amet, nec an dictas equidem appellantur, ut has commune accommodare. Mea illum, ludus solet idpro.</p></div>
    <div class="foot"><span class="copy">COPYRIGHT © | ALL RIGHTS RESERVED</span><span class="page">PAGE | 12</span></div>
  </div>

  <div class="slide media">
    <div class="band"></div>
    <div class="brand brand-mini">Copper Lantern</div>
    <h3 class="title-dark heading">Here Add Title<br>Short Text Here</h3>
    <div class="body">
      <p>Lorem ipsum dolor sit amet, consectetur adipiscing elit, sed do eiusmod tempor incididunt ut labore et dolore magna aliqua. Lorem ipsum dolor sit amet, consectetur adipiscing elit.</p>
      <p>Sed do eiusmod tempor incididunt ut labore et dolore magna aliqua. Ut enim ad minim veniam, quis nostrud exercitation ullamco laboris nisi ut aliquip.</p>
      <p>Ut enim ad minim veniam, quis nostrud exercitation ullamco laboris nisi ut aliquip.</p>
    </div>
    <svg class="laptop" viewBox="0 0 300 186">
      <rect x="26" y="0" width="248" height="168" rx="7" fill="#1b1f2a"/>
      <rect x="33" y="7" width="234" height="154" fill="#dfe6ef"/>
      <rect x="33" y="7" width="234" height="100" fill="#b9c8da"/>
      <text x="150" y="106" text-anchor="middle" font-family="Montserrat, sans-serif" font-weight="600" font-size="9" fill="#1e2538">Add your picture or Video</text>
      <path d="M0 170h300l-8 12H8z" fill="#c7cbd2"/>
      <rect x="130" y="170" width="40" height="3" rx="1.5" fill="#9aa0aa"/>
    </svg>
  </div>

  <div class="slide quiz">
    <div class="brand brand-mini">Copper Lantern</div>
    <h3 class="title-dark heading">Mini Quiz layout<br>Short Text Here</h3>
    <div class="q-bar">Here goes your Question?</div>
    <svg class="abs" style="left:0;top:0" width="551" height="310"><path d="M278 142v24M146 176v-10h264v10" fill="none" stroke="#9cc8f2"/></svg>
    <div class="ans" style="left:65px;top:176px">A. Answer</div>
    <div class="ans" style="left:292px;top:176px">C. Answer</div>
    <div class="ans" style="left:65px;top:230px">B. Answer</div>
    <div class="ans" style="left:292px;top:230px">D. Answer</div>
    <div class="foot"><span class="copy">COPYRIGHT © | ALL RIGHTS RESERVED</span><span class="page">PAGE | 14</span></div>
  </div>

  <div class="slide close">
    <div class="photo" role="img" aria-label="Blue-toned photo of a team working in an office"></div>
    <div class="dot"></div>
    <div class="brand">Copper Lantern</div>
    <p class="thanks">Thank You. <span>Contact Us.</span></p>
    <div class="contact">
      <span><svg width="6" height="6" viewBox="0 0 6 6"><circle cx="3" cy="3" r="3" fill="#27306b"/></svg>www.copper-lantern.com</span>
      <span><svg width="6" height="6" viewBox="0 0 6 6"><path d="M3 0a2 2 0 012 2c0 1.5-2 4-2 4S1 3.5 1 2a2 2 0 012-2z" fill="#27306b"/></svg>Here to write your Company adress</span>
      <span><svg width="6" height="6" viewBox="0 0 6 6"><path d="M1 0h1.5l.5 1.5-1 .8a3.5 3.5 0 001.7 1.7l.8-1 1.5.5V5a1 1 0 01-1 1A5 5 0 010 1a1 1 0 011-1z" fill="#27306b"/></svg>(555) 014-2280</span>
      <span><svg width="7" height="5" viewBox="0 0 7 5"><rect width="7" height="5" fill="#27306b"/><path d="M0 0l3.5 2.5L7 0" stroke="#fff" stroke-width=".6" fill="none"/></svg>hello@copper-lantern.com</span>
    </div>
  </div>

</main>
</body>
</html>
```